Falcrest security business card

Looking for a business card for my security company

Target Market(s)

Security

Industry/Entity Type

Security

Contact Information for Business Card

Name - Gil Marston. Title - General manager - direct 314 862.4490 website www. falcrestsecurityservices.example email - gil@ falcrestsecurityservices.example

Requirements
Must have
• Logo attached

```html
<!DOCTYPE html>
<html lang="en">
<head>
<meta charset="utf-8">
<title>Falcrest Security Services – Business Card</title>
<link rel="stylesheet" href="https://fonts.googleapis.com/css2?family=Open+Sans:wght@800&family=Roboto:wght@300;400&display=swap">
<style>
  :root {
    --stage: #979797;
    --paper: #ffffff;
    --ink: #000000;
    --gold: #c9a45a;
    --gold-light: #f3e6bd;
    --gold-dark: #a97f3e;
    --text-light: #ffffff;
  }
  * { margin: 0; padding: 0; box-sizing: border-box; }
  html, body {
    width: 1200px;
    height: 1200px;
    overflow: hidden;
    background: var(--stage);
  }
  .card {
    position: absolute;
    left: 141px;
    width: 918px;
    overflow: hidden;
  }
  .card--front { top: 67px; height: 524px; background: var(--ink); }
  .card--back  { top: 609px; height: 523px; background: var(--ink); }

  .front-top {
    position: absolute;
    left: 0; top: 0;
    width: 100%;
    height: 263px;
    background: var(--paper);
  }
  .gold-band {
    position: absolute;
    left: 0; top: 263px;
    width: 100%;
    height: 18px;
    background: linear-gradient(90deg, var(--gold-dark) 0%, var(--gold-light) 22%, var(--gold-dark) 50%, var(--gold-light) 78%, var(--gold-dark) 100%);
  }

  .wordmark {
    position: absolute;
    left: 0;
    width: 100%;
    text-align: center;
    font-family: "Open Sans", sans-serif;
    font-weight: 800;
    text-transform: uppercase;
    letter-spacing: 0.02em;
    line-height: 1;
  }
  .wordmark--front { top: 104px; font-size: 62px; color: var(--ink); }
  .wordmark--back  { top: 210px; font-size: 96px; color: var(--gold); }

  .person {
    position: absolute;
    left: 52px;
    top: 345px;
  }
  .person__name {
    font-family: "Open Sans", sans-serif;
    font-weight: 800;
    font-size: 40px;
    line-height: 1;
    text-transform: uppercase;
    background: linear-gradient(90deg, var(--gold-dark), var(--gold-light) 45%, var(--gold-dark));
    -webkit-background-clip: text;
    background-clip: text;
    color: transparent;
  }
  .person__title {
    margin-top: 12px;
    font-family: "Roboto", sans-serif;
    font-weight: 400;
    font-size: 25px;
    color: var(--text-light);
  }

  .contact {
    position: absolute;
    left: 446px;
    top: 347px;
    list-style: none;
  }
  .contact__row {
    display: flex;
    align-items: center;
    height: 39.5px;
    font-family: "Roboto", sans-serif;
    font-weight: 300;
    font-size: 24px;
    color: var(--text-light);
  }
  .contact__icon {
    width: 20px;
    height: 20px;
    margin-right: 20px;
    flex: none;
  }
</style>
</head>
<body>

<section class="card card--front">
  <div class="front-top"></div>
  <div class="wordmark wordmark--front">Falcrest</div>
  <div class="gold-band"></div>

  <div class="person">
    <div class="person__name">Gil Marston</div>
    <div class="person__title">General Manager</div>
  </div>

  <ul class="contact">
    <li class="contact__row">
      <svg class="contact__icon" viewBox="0 0 24 24" aria-hidden="true">
        <path fill="#c9a45a" d="M6.6 10.8c1.4 2.8 3.8 5.1 6.6 6.6l2.2-2.2c.3-.3.7-.4 1-.2 1.1.4 2.3.6 3.6.6.6 0 1 .4 1 1V20c0 .6-.4 1-1 1C10.6 21 3 13.4 3 4c0-.6.4-1 1-1h3.5c.6 0 1 .4 1 1 0 1.3.2 2.5.6 3.6.1.3 0 .7-.2 1l-2.3 2.2z"/>
      </svg>
      314 862 4490
    </li>
    <li class="contact__row">
      <svg class="contact__icon" viewBox="0 0 24 24" aria-hidden="true">
        <rect x="2" y="5" width="20" height="14" fill="#c9a45a"/>
        <path d="M2 5l10 7 10-7" fill="none" stroke="#000" stroke-width="1.6"/>
      </svg>
      gil@falcrestsecurityservices.example
    </li>
    <li class="contact__row">
      <svg class="contact__icon" viewBox="0 0 24 24" aria-hidden="true">
        <g fill="none" stroke="#c9a45a" stroke-width="2">
          <circle cx="12" cy="12" r="9"/>
          <ellipse cx="12" cy="12" rx="4" ry="9"/>
          <path d="M3 12h18M5 7h14M5 17h14"/>
        </g>
      </svg>
      falcrestsecurityservices.example
    </li>
  </ul>
</section>

<section class="card card--back">
  <div class="wordmark wordmark--back">Falcrest</div>
</section>

</body>
</html>
```